Business card for our large format printing and installation business

We want a professional looking business card for our business. We manufacture and install Signs.

On the back of the card add this info
Large Format Graphics Printing & Installations, Event Graphics, Banners, Posters, Vehicle Fleet Graphics, Boat Wraps, Wall Murals, Decals,Displays,Signs,Plaques,Digital Signs

On the Front of the card add the Tallowfern Signs logo, plus On the back of the card add the Orange Tallowfern Wraps logo. The 2 vector logos are attached to the design brief.

Target Market(s)

Local business owners

Contact Information for Business Card

Colors
f37122
f68d4e
f9ba93

Requirements
Must have
• On the Front of the card add the Tallowfern Signs logo, plus On the back of the card add the Orange Tallowfern Wraps logo. The 2 vector logos are attached to the design brief.

```html
<!DOCTYPE html>
<html lang="en">
<head>
<meta charset="utf-8">
<title>Tallowfern Signs – Business Card</title>
<link href="https://fonts.googleapis.com/css2?family=Arimo:wght@400;700&family=PT+Serif:wght@700&display=swap" rel="stylesheet">
<style>
  :root{
    --bg:#d9d9d9;
    --paper:#ffffff;
    --ink:#111111;
    --muted:#555555;
    --orange:#f37122;
    --orange-mid:#f68d4e;
    --orange-light:#f9ba93;
    --rule:#1a1a1a;
  }
  *{box-sizing:border-box;margin:0;padding:0}
  html,body{width:1200px;height:960px;overflow:hidden;background:var(--bg)}
  .stage{position:relative;width:1200px;height:960px}
  .card{
    position:absolute;width:600px;height:343px;background:var(--paper);
    box-shadow:0 6px 18px rgba(0,0,0,.25);overflow:hidden;
    font-family:"Arimo",Arial,sans-serif;color:var(--ink);
  }
  .card--front{left:70px;top:70px}
  .card--back{left:530px;top:547px}

  .wordmark{
    font-family:"Arimo",Arial,sans-serif;font-weight:700;color:var(--orange);
    display:flex;align-items:center;justify-content:center;gap:12px;line-height:1;
  }
  .wordmark__dot{width:22px;height:22px;border-radius:50%;background:var(--orange)}

  .card--front .wordmark{position:absolute;left:0;right:0;top:120px;font-size:52px}
  .card--front .site{
    position:absolute;left:0;right:0;top:238px;text-align:center;
    font-size:14px;letter-spacing:4px;color:var(--muted);
  }

  .card--back .wordmark{position:absolute;left:0;right:0;top:34px;font-size:40px}
  .card--back .wordmark__dot{width:18px;height:18px}
  .services{
    position:absolute;left:40px;right:40px;top:96px;text-align:center;
    font-size:11.5px;line-height:1.45;color:var(--muted);
  }
  .services strong{color:var(--ink);font-weight:700}

  .band{position:absolute;left:0;right:0;bottom:0;height:168px;display:flex}
  .panel{
    height:100%;
    background:radial-gradient(ellipse at 50% 55%,var(--orange-light) 0%,var(--orange-mid) 45%,var(--orange) 100%);
  }
  .panel--person{flex:0 0 325px;padding:30px 0 0;text-align:center}
  .divider{flex:0 0 9px;background:var(--paper);border-left:2px solid var(--rule);border-right:2px solid var(--rule)}
  .panel--contact{flex:1;padding:24px 0 0 26px}

  .person__name{font-family:"PT Serif",Georgia,serif;font-weight:700;font-size:22px}
  .person__title{font-family:"PT Serif",Georgia,serif;font-weight:700;font-size:15px;margin:2px 0 18px 90px}
  .person__address{font-size:15px;line-height:1.35}

  .contact{list-style:none}
  .contact li{display:flex;align-items:center;gap:10px;font-size:14.5px;line-height:23px}
  .contact svg{width:13px;height:13px;flex:none;fill:var(--ink)}
</style>
</head>
<body>
<main class="stage">

  <section class="card card--front" aria-label="Card front">
    <div class="wordmark"><span class="wordmark__dot"></span>Tallowfern Signs</div>
    <p class="site">www.tallowfernsigns.com</p>
  </section>

  <section class="card card--back" aria-label="Card back">
    <div class="wordmark"><span class="wordmark__dot"></span>Tallowfern Wraps</div>
    <p class="services"><strong>Large Format Graphics Printing &amp; Installations</strong><br>
      Event Graphics · Banners · Posters · Vehicle Fleet Graphics · Boat Wraps · Wall Murals<br>
      Decals · Displays · Signs · Plaques · Digital Signs</p>

    <div class="band">
      <div class="panel panel--person">
        <p class="person__name">Daniel Hartwell</p>
        <p class="person__title">President</p>
        <p class="person__address">412 Cedar Hollow Road<br>Juneau, Alaska 99801</p>
      </div>
      <div class="divider"></div>
      <div class="panel panel--contact">
        <ul class="contact">
          <li><svg viewBox="0 0 16 16"><path d="M3 1l3 3-2 2c1 2 4 5 6 6l2-2 3 3-2 2C7 15 1 9 1 3z"/></svg>555-014-2231</li>
          <li><svg viewBox="0 0 16 16"><path d="M4 0h8v16H4zM5.5 2v10h5V2z"/></svg>555-014-7702</li>
          <li><svg viewBox="0 0 16 16"><path d="M4 1h7v4H4zM1 6h14v7h-3v2H4v-2H1zM5 11v3h6v-3z"/></svg>555-014-3916</li>
          <li><svg viewBox="0 0 16 16"><path d="M0 3h16v10H0zM1.5 4.5L8 9l6.5-4.5V4H1.5z"/></svg>info@tallowfernsigns.com</li>
          <li><svg viewBox="0 0 16 16"><circle cx="8" cy="8" r="7.5"/></svg>www.tallowfernsigns.com</li>
        </ul>
      </div>
    </div>
  </section>

</main>
</body>
</html>
```